Kestro Vale - Dog Supplement Brand

Here a link to a word doc with all of my info.
Please read it carefully.
https://files.brindlepad.net/sheet/7QwLx2mTa8Rk3PzNv0eYc5Hj9UfGs46Bd1Oi-Lp-3/view?ref=shared
Its 2 pages. Home Page and Product Page.
Oh and btw: the poses I attached dont have a shadow, so it would be good if you added a shadow to the poses .
If you have any questions please let me know.
Target Market(s)
Dog Owners In UK
Industry/Entity Type
Dog supplements
Number of Pages Required
2 page
Requirements
Must have
- Home page and product page files. Super Hero Theme.

```html
<!DOCTYPE html>
<html lang="en">
<head>
<meta charset="utf-8">
<title>Kestro Vale – Home</title>
<link rel="stylesheet" href="https://fonts.googleapis.com/css2?family=Exo+2:ital,wght@0,600;0,800;1,700;1,800;1,900&family=Open+Sans:ital,wght@0,400;0,600;0,700;1,400&display=swap">
<style>
:root{
  --red:#e3262b;
  --orange:#e8541c;
  --dark:#232323;
  --black:#0c0c0c;
  --white:#ffffff;
  --yellow:#f2c200;
  --text:#222222;
  --muted:#6b6b6b;
  --navy:#1f2533;
  --green:#4f9a14;
  --blue:#1a7ad9;
}
*{box-sizing:border-box;margin:0;padding:0}
html,body{width:1200px;height:4604px;overflow:hidden}
body{position:relative;background:var(--white);font-family:"Open Sans",sans-serif;color:var(--text)}
.abs{position:absolute}
.display{font-family:"Exo 2",sans-serif;font-style:italic;font-weight:800}
.center{left:0;width:1200px;text-align:center}
.bg-layer{position:absolute;left:0;top:0}

/* header */
.site-header{position:absolute;left:0;top:0;width:1200px;height:75px;background:var(--white);z-index:5}
.menu-icon{position:absolute;left:72px;top:30px;width:26px}
.menu-icon span{display:block;height:3px;background:var(--text);margin-bottom:5px;border-radius:2px}
.brand{position:absolute;left:0;width:1200px;top:22px;text-align:center;font-family:"Exo 2",sans-serif;font-weight:800;font-size:26px;color:var(--black)}
.header-icons{position:absolute;right:72px;top:28px;display:flex;gap:18px}

/* hero */
.hero-kicker{left:72px;top:176px;color:var(--white);font-size:18px}
.hero-title{left:70px;top:196px;font-size:64px;color:var(--white);line-height:1}
.hero-title em{color:var(--yellow);font-style:inherit}
.hero-tag{left:72px;top:270px;font-size:22px;color:var(--white)}
.btn{position:absolute;display:block;text-align:center;font-family:"Exo 2",sans-serif;font-style:italic;font-weight:800;font-size:14px}
.btn-join{left:72px;top:322px;width:140px;height:40px;line-height:36px;background:var(--white);color:var(--black);border:2px solid var(--yellow);box-shadow:3px 3px 0 var(--yellow)}
.btn-red{background:var(--red);color:var(--white);box-shadow:3px 3px 0 #8d1114;height:36px;line-height:36px}
.hero-dog{left:615px;top:100px;width:500px;height:460px;border-radius:46% 46% 40% 40%;background:radial-gradient(circle at 50% 40%,#f2f2f2,#9a9a9a 55%,#2a2a2a 80%,rgba(0,0,0,0) 81%)}

.hi{top:508px;font-size:64px;color:var(--black)}
.hi-sub{top:582px;font-size:40px;color:var(--black)}
.intro{left:140px;width:920px;top:662px;text-align:center;font-size:16px;line-height:23px;color:#333}

/* offer */
.section-title{font-size:42px}
.offer-title{top:895px;color:var(--white)}
.shield{position:absolute;width:336px;height:290px;clip-path:path("M40 0 L120 0 Q168 28 216 0 L296 0 Q320 40 336 55 Q300 120 330 160 Q336 250 230 285 L168 290 L106 285 Q0 250 6 160 Q36 120 0 55 Q16 40 40 0 Z")}
.offer-label{position:absolute;width:336px;text-align:center;font-size:27px;color:var(--white);line-height:37px}

/* products */
.products-title{top:1872px;color:var(--black)}
.product-card{position:absolute;top:1957px;width:248px;height:265px;border:1px solid #d6d6d6;background:var(--white)}
.product-shot{position:absolute;left:40px;top:18px;width:168px;height:228px;border-radius:14px;background:linear-gradient(180deg,#f0f0f0 0 22%,#4aa82a 22% 88%,#ececec 88%)}
.product-meta{position:absolute;top:2236px;width:248px;text-align:center}
.product-meta small{display:block;font-size:11px;color:#444}
.product-meta strong{display:block;font-family:"Exo 2",sans-serif;font-style:italic;font-weight:800;font-size:18px;color:var(--text);margin-top:2px}
.price{display:block;font-size:12px;color:var(--red);font-weight:700;margin-top:6px}
.price s{color:#888;font-weight:400;font-size:10px}

/* testimonial */
.love-title{top:2465px;color:var(--white)}
.reviewer{left:400px;width:510px;text-align:center;color:var(--white)}
.review-name{top:2722px;font-size:26px}
.review-date{top:2760px;font-size:14px}
.review-text{left:285px;width:670px;top:2873px;text-align:center;color:var(--white);font-style:italic;font-size:15px;line-height:23px}
.pager{left:1045px;top:2816px;font-size:14px;font-weight:600;color:var(--white)}

/* vets */
.vets-title{top:3263px;color:var(--black)}
.video{left:287px;top:3335px;width:626px;height:365px;background:linear-gradient(180deg,#9aa5a8 0%,#e9c98b 38%,#6e6a5e 60%,#3e3a31 100%)}
.video-bar{position:absolute;left:0;bottom:0;width:100%;height:44px;background:rgba(0,0,0,.25)}
.play{position:absolute;left:22px;top:6px;width:64px;height:32px;background:#111;border-radius:3px}
.play:before,.play:after{content:"";position:absolute;top:9px;width:4px;height:14px;background:#fff}
.play:before{left:26px}.play:after{left:34px}
.track{position:absolute;left:96px;top:19px;width:374px;height:6px;background:#333}
.track i{display:block;width:62%;height:100%;background:#888}

/* why */
.why-title{top:3758px;color:var(--black)}
.why-card{position:absolute;top:3840px;width:336px;height:238px;border-radius:40px;color:var(--white);font-weight:700;font-size:22px;text-align:center;line-height:28px}
.why-card svg{position:absolute;left:138px;top:44px}
.why-card p{position:absolute;left:20px;width:296px;top:146px}
.why-green{background:radial-gradient(circle at 50% 35%,#8bd21f,var(--green) 60%,#2e6b09)}
.why-red{background:radial-gradient(circle at 50% 35%,#ff4b4f,var(--red) 60%,#8d0d12)}
.why-blue{background:radial-gradient(circle at 50% 35%,#4fb7ff,var(--blue) 60%,#0b3f8f)}

/* footer */
.footer-head{top:4285px;font-size:20px;font-weight:600;color:var(--white)}
.footer-links{list-style:none;top:4335px;font-size:13px;color:#cfcfcf;line-height:30px}
.news-input{left:640px;top:4333px;width:270px;height:36px;background:var(--white);font-size:11px;color:#555;padding:10px 14px}
.news-btn{left:640px;top:4378px;width:270px;height:36px;background:var(--red);color:var(--white);font-size:12px;font-weight:700;text-align:center;line-height:36px}
.social{top:4337px;width:30px;height:30px;border:1px solid #555;background:#1b1b1b}
.copyright{top:4517px;font-size:12px;color:#cfcfcf}
.copyright em{color:var(--red);font-style:normal}
.pay{top:4512px;width:36px;height:22px;border-radius:3px}
</style>
</head>
<body>

<svg class="bg-layer" width="1200" height="4604" viewBox="0 0 1200 4604" aria-hidden="true">
  <defs>
    <linearGradient id="heroGrad" x1="0" y1="0" x2="1" y2="1">
      <stop offset="0" stop-color="#d93a12"/><stop offset=".5" stop-color="#e8541c"/><stop offset="1" stop-color="#c41f1a"/>
    </linearGradient>
    <linearGradient id="loveGrad" x1="0" y1="0" x2="1" y2="0">
      <stop offset="0" stop-color="#b71c1c"/><stop offset=".6" stop-color="#d83a30"/><stop offset="1" stop-color="#c9261f"/>
    </linearGradient>
  </defs>
  <path d="M0 75 H950 Q1120 80 1130 200 Q1135 330 1050 380 Q990 420 960 470 Q900 540 820 500 Q720 440 620 390 Q520 350 430 400 Q300 470 180 510 Q80 540 0 470 Z" fill="url(#heroGrad)"/>
  <path d="M0 795 Q600 780 1200 790 V1890 Q980 1810 600 1830 Q250 1845 0 1890 Z" fill="var(--dark)"/>
  <path d="M0 790 Q300 870 600 840 Q900 810 1200 790 Z" fill="var(--white)"/>
  <rect x="0" y="2452" width="1200" height="758" fill="url(#loveGrad)"/>
  <path d="M0 2452 H1200 V2620 Q900 2540 600 2580 Q300 2620 0 2610 Z" fill="#b2151a"/>
  <path d="M0 2610 Q300 2580 560 2590 L580 2700 Q420 2760 300 2700 Q150 2640 0 2700 Z" fill="var(--white)"/>
  <path d="M0 2700 V3210 H700 Q760 3130 880 3100 Q1000 3080 1050 3040 Q1000 2990 880 2990 Q820 2960 800 2900 Q760 2780 700 2700 Q560 2640 440 2680 Q330 2700 280 2760 Q260 2860 200 2900 Q80 2950 0 2950 Z" fill="var(--white)"/>
  <path d="M520 2640 Q620 2600 760 2660 Q830 2700 830 2780 Q850 2830 950 2845 Q1005 2900 975 2965 Q910 3015 770 3020 Q730 3070 740 3130 Q720 3210 640 3200 Q560 3180 560 3110 Q540 3040 420 3015 Q235 2995 245 2910 Q250 2840 440 2825 Q470 2760 460 2710 Q470 2660 520 2640 Z" fill="var(--navy)"/>
  <path d="M0 4190 Q300 4110 600 4150 Q900 4190 1200 4120 V4604 H0 Z" fill="var(--black)"/>
</svg>

<header class="site-header">
  <div class="menu-icon"><span></span><span></span><span></span></div>
  <div class="brand">Kestro Vale</div>
  <div class="header-icons">
    <svg width="16" height="16" viewBox="0 0 16 16" fill="none" stroke="#333" stroke-width="1.6"><circle cx="7" cy="7" r="5"/><path d="M11 11l4 4"/></svg>
    <svg width="16" height="16" viewBox="0 0 16 16" fill="none" stroke="#333" stroke-width="1.6"><circle cx="8" cy="5" r="3.5"/><path d="M2 15c1-4 11-4 12 0"/></svg>
    <svg width="16" height="16" viewBox="0 0 16 16" fill="none" stroke="#333" stroke-width="1.6"><rect x="3" y="5" width="10" height="10"/><path d="M5.5 5V3.5a2.5 2.5 0 015 0V5"/></svg>
  </div>
</header>

<div class="abs hero-kicker">Join Forces With</div>
<div class="abs hero-title display">Kestro <em>Vale</em></div>
<div class="abs hero-tag display">&amp; Let Him Be Your Beloved Dog's Hero!</div>
<a class="btn btn-join">Join Forces</a>
<div class="abs hero-dog" role="img" aria-label="Superhero husky mascot in red cape flying"></div>

<div class="abs center hi display">Hi!</div>
<div class="abs center hi-sub display">I am Kestro Vale</div>
<p class="abs intro">Lorem ipsum dolor sit amet, consectetur adipisicing elit, sed do eiusmod tempor incididunt ut labore et dolore magna aliqua. Ut enim ad minim veniam, quis nostrud exercitation ullamco laboris nisi ut aliquip ex ea commodo consequat...</p>
<a class="btn btn-red" style="left:530px;top:760px;width:140px">Read More</a>

<h2 class="abs center section-title display offer-title">Here's What I Offer</h2>
<div class="shield" style="left:72px;top:980px;background:radial-gradient(circle at 50% 45%,#3a3a3a,#1e1e1e 45%,#eab308 46%)" role="img" aria-label="Black pug on yellow background"></div>
<div class="shield" style="left:432px;top:980px;background:linear-gradient(180deg,#b9d3e6,#4a89b0 55%,#2a5b7c)" role="img" aria-label="Happy brown dog by the sea"></div>
<div class="shield" style="left:792px;top:980px;background:radial-gradient(circle at 50% 45%,#d9a55a,#8a5a25 60%,#3a3a2a)" role="img" aria-label="Golden retriever puppy with a stick"></div>
<div class="offer-label display" style="left:72px;top:1298px">Kestro Vale Calm</div>
<div class="offer-label display" style="left:432px;top:1298px">Kestro Vale Joint Support</div>
<div class="offer-label display" style="left:792px;top:1298px">Kestro Vale MultiVits</div>
<div class="shield" style="left:72px;top:1383px;background:radial-gradient(circle at 50% 45%,#f0f0f0,#9a9a9a 60%,#555)" role="img" aria-label="Black and white dog smiling"></div>
<div class="shield" style="left:432px;top:1383px;background:radial-gradient(circle at 50% 45%,#a0602e,#3b2416 60%,#e8cfc4 61%)" role="img" aria-label="Jack Russell terrier portrait"></div>
<div class="shield" style="left:792px;top:1383px;background:radial-gradient(circle at 50% 45%,#e0a86a,#b06a2a 55%,#e8d3c6 56%)" role="img" aria-label="Beagle smiling"></div>
<div class="offer-label display" style="left:72px;top:1701px">Kestro Vale Omega 369</div>
<div class="offer-label display" style="left:432px;top:1701px">Kestro Vale Probiotics</div>
<div class="offer-label display" style="left:792px;top:1701px">Kestro Vale Digestive Support</div>

<h2 class="abs center section-title display products-title">Featured Products</h2>
<div class="product-card" style="left:70px"><div class="product-shot" role="img" aria-label="Multivitamin tub"></div></div>
<div class="product-card" style="left:341px"><div class="product-shot" role="img" aria-label="Joint support powder tub"></div></div>
<div class="product-card" style="left:611px"><div class="product-shot" role="img" aria-label="Multivitamin tub"></div></div>
<div class="product-card" style="left:881px"><div class="product-shot" role="img" aria-label="Multivitamin tub"></div></div>
<div class="product-meta" style="left:70px"><small>Calm Kestro Trial</small><strong>Deliver Every 30 Days</strong><span class="price">£10.00 GBP <s>£39.95 GBP</s></span></div>
<div class="product-meta" style="left:341px"><small>Kestro Vale</small><strong>Joint Support - 150g Powder</strong><span class="price">£24.00 GBP <s>£29.95 GBP</s></span></div>
<div class="product-meta" style="left:611px"><small>Calm Kestro Trial</small><strong>Deliver Every 120 Days</strong><span class="price">£10.00 GBP <s>£39.95 GBP</s></span></div>
<div class="product-meta" style="left:881px"><small>Calm Kestro Trial</small><strong>Deliver Every 30 Days</strong><span class="price">£10.00 GBP <s>£39.95 GBP</s></span></div>
<a class="btn btn-red" style="left:517px;top:2357px;width:165px">View all Products</a>

<div class="abs" style="left:760px;top:2540px;width:440px;height:520px;background:radial-gradient(circle at 45% 35%,rgba(230,90,60,.6),rgba(180,20,20,0) 70%)" role="img" aria-label="Red setter dog in autumn woods"></div>
<h2 class="abs center section-title display love-title">People Love Me</h2>
<div class="abs" style="left:585px;top:2548px;width:140px;height:140px;border-radius:50%;border:4px solid var(--white);background:radial-gradient(circle at 50% 45%,#f1c7a8,#6b4a2e 70%)" role="img" aria-label="Reviewer portrait"></div>
<div class="abs reviewer review-name">Maren Holt</div>
<div class="abs reviewer review-date">January 11, 2022</div>
<div class="abs" style="left:830px;top:2826px;width:208px;height:1px;background:var(--white)"></div>
<div class="abs pager">PREV | NEXT</div>
<p class="abs review-text">Sed ut perspiciatis unde omnis iste natus error sit voluptatem accusantium doloremque laudantium, totam rem aperiam, eaque ipsa quae ab illo inventore veritatis et quasi architecto beatae vitae dicta sunt explicabo. &nbsp;Nemo enim ipsam voluptatem quia voluptas sit aspernatur aut odit aut fugit, sed quia consequuntur magni</p>
<svg class="abs" style="left:575px;top:3008px" width="50" height="38" viewBox="0 0 50 38" fill="#5a6070" aria-hidden="true"><path d="M0 0h20v20l-8 18H4l6-16H0z"/><path d="M28 0h20v20l-8 18h-8l6-16h-10z"/></svg>
<div class="abs" style="left:72px;top:2750px;width:200px;height:330px;border-radius:45% 45% 30% 30%;background:radial-gradient(circle at 50% 40%,#f4f4f4,#bdbdbd 50%,rgba(200,20,20,.8) 75%,rgba(0,0,0,0) 76%)" role="img" aria-label="Husky mascot sitting with red cape"></div>

<h2 class="abs center section-title display vets-title">Approved By Expert Vets</h2>
<div class="abs video" role="img" aria-label="Video of a dog playing with a frisbee on the beach at sunset">
  <div class="video-bar"><div class="play"></div><div class="track"><i></i></div></div>
</div>

<h2 class="abs center section-title display why-title">Why Choose Us</h2>
<div class="why-card why-green" style="left:72px">
  <svg width="60" height="60" viewBox="0 0 60 60" fill="none" stroke="#fff" stroke-width="2.5"><circle cx="30" cy="30" r="27"/><path d="M30 46V22M30 30l-8-8M30 36l8-8"/></svg>
  <p>Only Organic &amp; Natural Ingredients</p>
</div>
<div class="why-card why-red" style="left:432px">
  <svg width="60" height="60" viewBox="0 0 60 60" fill="none" stroke="#fff" stroke-width="2.5"><circle cx="30" cy="30" r="22"/><path d="M20 26h20M22 34l16-16"/></svg>
  <p>20% off for all Kestro Vale Squad members</p>
</div>
<div class="why-card why-blue" style="left:792px">
  <svg width="60" height="60" viewBox="0 0 60 60" fill="none" stroke="#fff" stroke-width="2.5"><path d="M6 16h30v24H6zM36 24h10l8 8v8H36z"/><circle cx="16" cy="42" r="4"/><circle cx="44" cy="42" r="4"/></svg>
  <p>Free next Day UK Delivery</p>
</div>

<div class="abs footer-head" style="left:70px">Quick Links</div>
<ul class="abs footer-links" style="left:70px"><li>Join Kestro Vale!</li><li>Browse Supplements</li><li>About Kestro Vale</li><li>Reviews</li><li>Need Help?</li><li>Legal</li></ul>
<div class="abs footer-head" style="left:376px">Other Link</div>
<ul class="abs footer-links" style="left:376px"><li>Privacy Policy</li><li>My Account</li><li>My cart</li><li>Search</li><li>Terms &amp; Conditions</li></ul>
<div class="abs footer-head" style="left:640px">Newsletter</div>
<div class="abs news-input">Enter Your Email:</div>
<div class="abs news-btn">SUBSCRIBE</div>
<div class="abs footer-head" style="left:1020px">Follow Us</div>
<div class="abs social" style="left:1020px"></div>
<div class="abs social" style="left:1058px"></div>
<div class="abs social" style="left:1097px"></div>
<div class="abs center copyright">Copyright © 2022 <em>Kestro Vale</em>. All Rights Reserved.</div>
<div class="abs pay" style="left:972px;background:#e6e6e6"></div>
<div class="abs pay" style="left:1012px;background:#2b3f91"></div>
<div class="abs pay" style="left:1052px;background:#3aa0d8"></div>
<div class="abs pay" style="left:1092px;background:#f2f2f2"></div>

</body>
</html>
```